U.S. based testing, inspection, and certification (TIC) company needs a new PowerPoint template.

We need a new PowerPoint template (deck, slide deck) for our U.S. based company with international capabilities for performing numerous testing, inspection, and certification (TIC) services. Our primary services include calibration, chemical analysis, consulting engineering, environmental simulation, forensic engineering, materials testing, mechanical testing, and nondestructive testing. Industries we serve are aerospace/aviation, automotive, chemical, commercial properties, construction, consumer products, defense, energy storage, healthcare, insurance/legal, life science, manufacturing, oil & gas, power generation, pulp & paper, and telecommunications. https://qorvenlab.com/

Guideline hex colors: #29aae2, #0b1f3b, #fb6805 (use orange more subtly)

The final design should communicate:
1. Trust, Integrity, and Independence
2. Technical Expertise and Accuracy
3. Efficiency and Speed
4. Value-Added Partnership

Our current branding reflects a variety of styles, several of which have been included as attachments for reference in this project. While these examples showcase the direction we have taken in the past, we are not limited to them and remain open to exploring fresh, innovative design that is simple, clean, and with plenty of space to add content for each slide. We welcome creative concepts that build on or reimagine our existing identity to better align with our evolving vision.

```html
<!DOCTYPE html>
<html lang="en">
<head>
<meta charset="utf-8">
<title>Qorven Technical Services — Presentation Template</title>
<link href="https://fonts.googleapis.com/css2?family=Roboto:ital,wght@0,400;0,500;0,700;0,900;1,400&display=swap" rel="stylesheet">
<style>
  :root{
    --navy:#0b1f3b;
    --blue:#29aae2;
    --blue-deep:#0a8ad8;
    --orange:#fb6805;
    --ink:#0b1f3b;
    --text:#1d2530;
    --muted:#c9ced6;
    --stage:#3d3d3d;
    --white:#ffffff;
  }
  *{box-sizing:border-box;margin:0;padding:0}
  html,body{width:1200px;height:1127px;overflow:hidden;background:var(--stage)}
  body{font-family:'Roboto',sans-serif;color:var(--text);position:relative}
  .slide{position:absolute;width:516px;height:290px;background:var(--white);overflow:hidden}
  .slide--cover{left:69px;top:106px;background:var(--navy)}
  .slide--about{left:615px;top:106px}
  .slide--services{left:69px;top:417px}
  .slide--industries{left:615px;top:417px}
  .slide--why{left:69px;top:731px}
  .slide--contact{left:615px;top:731px}
  .art{position:absolute;inset:0;width:516px;height:290px}
  .abs{position:absolute}
  .title{font-weight:700;color:var(--ink);font-size:22px;letter-spacing:-.2px;line-height:1}
  .subtitle{color:var(--blue-deep);font-weight:500;font-size:14px;line-height:1.2}
  .rule{position:absolute;height:2px;width:48px;background:var(--orange)}
  .body-copy{font-size:6.6px;line-height:1.25;color:var(--text)}
  .dots{position:absolute;display:flex;gap:5px}
  .dots i{width:2px;height:2px;border-radius:50%;background:var(--muted)}

  /* cover */
  .brand{left:30px;top:35px;color:var(--white)}
  .brand__name{font-weight:900;font-size:25px;letter-spacing:2px;line-height:1}
  .brand__tag{font-size:8.2px;margin-top:3px}
  .cover__headline{left:30px;top:106px;color:var(--white);font-weight:700;font-size:15px;line-height:18px}
  .cover__headline span{color:var(--blue)}
  .cover__lead{left:30px;top:184px;color:var(--white);font-size:10px;line-height:12.6px}
  .cover__tagline{left:30px;top:224px;width:162px;border-top:1px solid rgba(255,255,255,.35);border-bottom:1px solid rgba(255,255,255,.35);padding:4px 0 3px 26px;color:var(--white);font-style:italic;font-size:10px;line-height:11.6px}
  .cover__tagline svg{position:absolute;left:3px;top:6px}

  /* about */
  .divider-v{position:absolute;width:1px;background:#c8ccd2}
  .values{left:288px;top:80px;list-style:none}
  .values li{display:flex;align-items:center;height:32.6px;font-size:7.6px;font-weight:500;color:var(--ink)}
  .values svg{width:14px;height:14px;margin-right:12px;flex:none}

  /* services */
  .svc-list{list-style:none;position:absolute}
  .svc-list li{display:flex;align-items:center;height:26px;font-size:8px;color:var(--text);position:relative}
  .svc-list li::after{content:"";position:absolute;left:23px;right:0;bottom:-1px;border-bottom:1px solid #d3d7dc}
  .svc-list li:last-child::after{display:none}
  .svc-list svg{width:11px;height:11px;margin-right:12px;flex:none}
  .footnote{color:var(--blue-deep);font-weight:500;font-size:7.6px;line-height:8.4px}

  /* industries */
  .industry{position:absolute;width:68px;text-align:center;font-size:6.4px;font-weight:500;line-height:7px;color:var(--ink)}
  .industry svg{display:block;margin:0 auto 4px;width:24px;height:24px}
  .sep{position:absolute;width:1px;height:30px;background:#d3d7dc}
  .callout{left:29px;top:249px;border-left:2px solid var(--blue-deep);padding-left:5px;color:var(--blue-deep);font-size:9px;line-height:10px}

  /* why */
  .reason{position:absolute;left:34px;display:flex;gap:8px}
  .reason__icon{width:19px;height:19px;border-radius:50%;background:var(--navy);flex:none;display:flex;align-items:center;justify-content:center;margin-top:2px}
  .reason h3{color:var(--blue-deep);font-weight:500;font-size:9.6px;line-height:10px}
  .reason p{font-size:6px;line-height:7px;color:var(--text)}

  /* contact */
  .contact__title{left:29px;top:31px;font-weight:700;color:var(--ink);font-size:24px;line-height:27px}
  .contact__title span{color:var(--blue-deep)}
  .benefit{position:absolute;width:80px;text-align:center;font-size:8px;line-height:8.6px;color:var(--text)}
  .benefit svg{display:block;margin:0 auto 5px;width:20px;height:20px}
  .cta{left:0;top:246px;width:116px;height:30px;background:var(--navy);color:var(--white);font-weight:700;font-size:12px;display:flex;align-items:center;padding-left:29px}
  .cta-arrow{left:113px;top:246px}
  .reach{position:absolute;top:250px;display:flex;align-items:center;gap:3px;color:var(--ink)}
  .reach small{display:block;font-size:5.4px;line-height:5px}
  .reach b{display:block;font-size:10px;line-height:11px;font-weight:700}
</style>
</head>
<body>

<!-- Cover -->
<section class="slide slide--cover">
  <svg class="art" viewBox="0 0 516 290">
    <defs>
      <linearGradient id="labGrad" x1="0" y1="0" x2="1" y2="1">
        <stop offset="0" stop-color="#c6d3e3"/><stop offset=".45" stop-color="#7f93ad"/><stop offset="1" stop-color="#24406a"/>
      </linearGradient>
    </defs>
    <polygon points="312,0 516,0 516,290 244,290" fill="url(#labGrad)" role="img" aria-label="Photograph: laboratory microscope objectives over a sample slide"/>
    <polygon points="326,185 412,185 373,290 302,290" fill="var(--blue-deep)"/>
    <polygon points="496,165 516,120 516,290 490,290" fill="var(--blue-deep)"/>
  </svg>
  <div class="abs brand"><div class="brand__name">QORVEN</div><div class="brand__tag">Qorven Technical Services</div></div>
  <h1 class="abs cover__headline">YOUR TRUSTED PARTNER<br>IN <span>TESTING, INSPECTION</span><br><span>&amp; CERTIFICATION</span></h1>
  <div class="rule" style="left:30px;top:172px"></div>
  <p class="abs cover__lead">Delivering Confidence Through Precision,<br>Innovation, and Independent Expertise</p>
  <div class="abs cover__tagline">
    <svg width="18" height="18" viewBox="0 0 20 20" fill="none" stroke="#fff" stroke-width="1"><circle cx="9" cy="9" r="8"/><ellipse cx="9" cy="9" rx="3.5" ry="8"/><path d="M1 9h16M2.5 5h13M2.5 13h13"/></svg>
    Trusted Solutions Across<br>Critical Industries Worldwide
  </div>
</section>

<!-- Who we are -->
<section class="slide slide--about">
  <h2 class="abs title" style="left:29px;top:64px">WHO WE ARE</h2>
  <p class="abs subtitle" style="left:29px;top:89px;font-size:15px;line-height:18px">Independent Expertise.<br>Global Capability.</p>
  <div class="rule" style="left:29px;top:133px"></div>
  <div class="abs body-copy" style="left:29px;top:146px;width:160px">
    <p>For decades, we have helped organizations verify performance, ensure compliance, and reduce risk through comprehensive testing, inspection, engineering, and certification services.</p>
    <p style="margin-top:6px">Our multidisciplinary teams combine advanced technology with deep technical knowledge to provide objective, accurate, and timely results that support confident decision-making.</p>
  </div>
  <div class="divider-v" style="left:240px;top:56px;height:181px"></div>
  <ul class="abs values">
    <li><svg viewBox="0 0 16 16" fill="none" stroke="var(--blue-deep)" stroke-width="1.2"><path d="M8 1.5l5.5 2v4c0 3.5-2.5 6-5.5 7-3-1-5.5-3.5-5.5-7v-4z"/><path d="M8 5.5v5M5.5 8h5"/></svg>Integrity in every evaluation</li>
    <li><svg viewBox="0 0 16 16" fill="none" stroke="var(--blue-deep)" stroke-width="1.2"><circle cx="8" cy="8" r="5.5"/><path d="M8 0.5v4M8 11.5v4M0.5 8h4M11.5 8h4"/></svg>Technical excellence backed by experience</li>
    <li><svg viewBox="0 0 16 16" fill="none" stroke="var(--blue-deep)" stroke-width="1.2"><path d="M8 2v12M3 4h10M5 14h6M3 4l-2 5h4zM13 4l-2 5h4z"/></svg>Independent and unbiased reporting</li>
    <li><svg viewBox="0 0 16 16" fill="none" stroke="var(--blue-deep)" stroke-width="1.2"><circle cx="4" cy="4" r="1.5"/><circle cx="8" cy="3.5" r="1.5"/><circle cx="12" cy="4" r="1.5"/><path d="M2 13V8h4v5M6 13V7h4v6M10 13V8h4v5"/></svg>Customer-focused collaboration</li>
    <li><svg viewBox="0 0 16 16" fill="none" stroke="var(--blue-deep)" stroke-width="1.4"><circle cx="8" cy="6" r="4"/><path d="M5 9.5L3.5 15 8 13l4.5 2L11 9.5"/></svg>Commitment to quality and safety</li>
  </ul>
  <div class="dots" style="left:416px;top:258px"><i></i><i></i><i></i><i></i><i></i><i></i><i></i></div>
  <div class="dots" style="left:416px;top:263px"><i></i><i></i><i></i><i></i><i></i><i></i><i></i></div>
</section>

<!-- Core services -->
<section class="slide slide--services">
  <svg class="art" viewBox="0 0 516 290">
    <defs>
      <linearGradient id="techGrad" x1="0" y1="0" x2="1" y2="1">
        <stop offset="0" stop-color="#a9bdd4"/><stop offset=".5" stop-color="#4a678c"/><stop offset="1" stop-color="#15294a"/>
      </linearGradient>
    </defs>
    <polygon points="422,0 428,0 370,127 430,250 424,250 364,127" fill="#d9dde2"/>
    <polygon points="428,0 516,0 516,290 440,290 370,127" fill="url(#techGrad)" role="img" aria-label="Photograph: engineer in safety glasses working at a lab station"/>
    <polygon points="383,290 516,157 516,290" fill="var(--blue-deep)"/>
  </svg>
  <h2 class="abs title" style="left:31px;top:33px">OUR CORE SERVICES</h2>
  <p class="abs subtitle" style="left:31px;top:59px">Comprehensive Technical Solutions</p>
  <ul class="svc-list" style="left:41px;top:98px;width:170px">
    <li><svg viewBox="0 0 12 12" fill="none" stroke="var(--navy)" stroke-width="1"><path d="M2 1v10M6 1v10M10 1v10"/><path d="M1 4h2M5 7h2M9 3h2" stroke-width="2"/></svg>Calibration Services</li>
    <li><svg viewBox="0 0 12 12" fill="none" stroke="var(--navy)" stroke-width="1"><path d="M4.5 1h3M5 1v3.5L2 11h8L7 4.5V1M3.5 8h5"/></svg>Chemical Analysis</li>
    <li><svg viewBox="0 0 12 12" fill="none" stroke="var(--blue-deep)" stroke-width="1"><path d="M3 11h6M6 11V7l3-4M4 5l2 2M8 2l2 1"/></svg>Consulting Engineering</li>
    <li><svg viewBox="0 0 12 12" fill="none" stroke="var(--navy)" stroke-width="1"><rect x="1.5" y="1.5" width="7" height="9"/><path d="M3 4h4M3 6h4M3 8h2"/><path d="M8 9c1-2 3-1 3 0" stroke="var(--blue-deep)"/></svg>Environmental Simulation</li>
    <li><svg viewBox="0 0 12 12" fill="none" stroke="var(--blue-deep)" stroke-width="1"><path d="M2 1h8M2 11h8M3 1c0 3 6 3 6 5s-6 2-6 5M9 1c0 3-6 3-6 5s6 2 6 5"/></svg>Forensic Engineering</li>
  </ul>
  <div class="divider-v" style="left:174px;top:98px;height:122px"></div>
  <ul class="svc-list" style="left:185px;top:98px;width:170px">
    <li><svg viewBox="0 0 12 12" fill="none" stroke="var(--navy)" stroke-width="1"><path d="M1 3l5-2 5 2v6l-5 2-5-2z M1 3l5 2 5-2M6 5v6"/><path d="M6 5l5-2v6l-5 2z" fill="var(--blue)" stroke="none"/></svg>Materials Testing</li>
    <li><svg viewBox="0 0 12 12" fill="none" stroke="var(--navy)" stroke-width="1"><circle cx="6" cy="6" r="2"/><circle cx="6" cy="6" r="4.2" stroke-dasharray="2 1.3"/></svg>Mechanical Testing</li>
    <li><svg viewBox="0 0 12 12" fill="none" stroke="var(--navy)" stroke-width="1"><path d="M3 8.5A2.5 2.5 0 0 1 3.5 3.6 3 3 0 0 1 9.3 4.5 2 2 0 0 1 9 8.5z"/><circle cx="6" cy="10" r="1" stroke="var(--blue-deep)"/></svg>Nondestructive Testing (NDT)</li>
    <li><svg viewBox="0 0 12 12" fill="none" stroke="var(--navy)" stroke-width="1"><circle cx="5" cy="5" r="3.5"/><path d="M7.5 7.5L11 11"/><path d="M3.5 5l1 1 2-2" stroke="var(--blue-deep)"/></svg>Failure Analysis</li>
    <li><svg viewBox="0 0 12 12" fill="none" stroke="var(--navy)" stroke-width="1"><circle cx="6" cy="6" r="4.5" stroke-dasharray="2.2 .8"/><path d="M4 6l1.5 1.5L8.5 4.5"/></svg>Inspection &amp; Compliance Verification</li>
  </ul>
  <p class="abs footnote" style="left:30px;top:245px">Every project is executed with precision, efficiency, and<br>internationally recognized quality standards.</p>
</section>

<!-- Industries -->
<section class="slide slide--industries">
  <svg class="art" viewBox="0 0 516 290">
    <polygon points="392,0 400,0 516,116 516,124" fill="#d9dde2"/>
    <polygon points="400,0 516,0 516,116" fill="var(--blue-deep)"/>
  </svg>
  <h2 class="abs title" style="left:28px;top:33px">INDUSTRIES WE SERVE</h2>
  <p class="abs subtitle" style="left:28px;top:59px">Supporting Critical Industries Worldwide</p>
  <div class="rule" style="left:28px;top:98px"></div>

  <div class="industry" style="left:16px;top:108px"><svg viewBox="0 0 24 24" fill="none" stroke="var(--navy)" stroke-width="1.2"><path d="M2 12h17a3 3 0 0 0 0-2H2zM9 10L6 3h2l6 7M9 12l-3 8h2l6-8M3 10l-1-3h1.5L6 10"/></svg>Aerospace &amp;<br>Aviation</div>
  <div class="sep" style="left:85px;top:114px"></div>
  <div class="industry" style="left:85px;top:108px"><svg viewBox="0 0 24 24" fill="none" stroke="var(--navy)" stroke-width="1.2"><path d="M3 15v-4l3-5h12l3 5v4z M3 11h18"/><circle cx="7" cy="18" r="2" stroke="var(--blue-deep)"/><circle cx="17" cy="18" r="2" stroke="var(--blue-deep)"/><path d="M9 18h6" stroke="var(--blue-deep)"/></svg>Automotive</div>
  <div class="sep" style="left:154px;top:114px"></div>
  <div class="industry" style="left:153px;top:108px"><svg viewBox="0 0 24 24" fill="none" stroke="var(--navy)" stroke-width="1.2"><path d="M4 21V7h4v14M10 21V4h4v17M16 21v-8h4v8M3 21h18"/><rect x="11" y="13" width="2" height="4" fill="var(--blue-deep)" stroke="none"/></svg>Chemical</div>
  <div class="sep" style="left:224px;top:114px"></div>
  <div class="industry" style="left:224px;top:108px"><svg viewBox="0 0 24 24" fill="none" stroke="var(--navy)" stroke-width="1.2"><path d="M8 22V3M12 22V3M8 6l4 0M8 10h4M8 14h4M8 18h4M3 5h19M19 5v6M5 22h10"/><path d="M18 12h2v2h-2z" fill="var(--blue-deep)" stroke="none"/></svg>Construction</div>
  <div class="sep" style="left:293px;top:114px"></div>
  <div class="industry" style="left:293px;top:108px"><svg viewBox="0 0 24 24" fill="none" stroke="var(--navy)" stroke-width="1.2"><path d="M12 2l8 3v6c0 6-4 9-8 11-4-2-8-5-8-11V5z"/><path d="M12 5l5 2v4c0 4-2.5 6-5 7.5z" fill="var(--blue-deep)" stroke="none"/></svg>Defense</div>
  <div class="sep" style="left:362px;top:114px"></div>
  <div class="industry" style="left:361px;top:108px"><svg viewBox="0 0 24 24" fill="none" stroke="var(--navy)" stroke-width="1.2"><circle cx="16" cy="7" r="3" stroke="var(--blue-deep)"/><path d="M16 1v2M16 11v2M22 7h-2M12 7h-2M20 3l-1.4 1.4M13.4 9.6L12 11M20 11l-1.4-1.4"/><path d="M3 21v-6h4l3-3M7 15v5h3v-3"/></svg>Energy Storage</div>

  <div class="industry" style="left:16px;top:168px"><svg viewBox="0 0 24 24" fill="none" stroke="var(--navy)" stroke-width="1.2"><rect x="3" y="7" width="16" height="12" rx="1"/><path d="M1 21h20M11 10v6M8 13h6"/><path d="M17 3a4 4 0 0 1 4 4M17 5a2 2 0 0 1 2 2" stroke="var(--blue-deep)"/></svg>Healthcare &amp;<br>Life Sciences</div>
  <div class="sep" style="left:85px;top:174px"></div>
  <div class="industry" style="left:85px;top:168px"><svg viewBox="0 0 24 24" fill="none" stroke="var(--navy)" stroke-width="1.2"><path d="M2 22V10l5 3v-3l5 3v-3l5 3V4h4v18z"/><path d="M6 17h2M10 17h2M14 17h2" stroke="var(--blue-deep)"/></svg>Manufacturing</div>
  <div class="sep" style="left:154px;top:174px"></div>
  <div class="industry" style="left:153px;top:168px"><svg viewBox="0 0 24 24" fill="none" stroke="var(--navy)" stroke-width="1.2"><path d="M3 5l10-3 2 5-10 3zM11 8l-3 14M14 8l4 14M9 16h7M5 22h16"/><path d="M3 5c-1 3 1 6 1 9" stroke="var(--blue-deep)"/></svg>Oil &amp; Gas</div>
  <div class="sep" style="left:224px;top:174px"></div>
  <div class="industry" style="left:224px;top:168px"><svg viewBox="0 0 24 24" fill="none" stroke="var(--navy)" stroke-width="1.2"><circle cx="12" cy="8" r="1.5"/><path d="M8 4a6 6 0 0 0 0 8M16 4a6 6 0 0 1 0 8M5 1.5a10 10 0 0 0 0 13M19 1.5a10 10 0 0 1 0 13" stroke="var(--blue-deep)"/><path d="M12 10l-5 12M12 10l5 12M9 17h6M3 22h18"/></svg>Telecommunications</div>
  <div class="sep" style="left:293px;top:174px"></div>
  <div class="industry" style="left:293px;top:168px"><svg viewBox="0 0 24 24" fill="none" stroke="var(--navy)" stroke-width="1.2"><path d="M12 2v18M4 5h16M7 22h10M4 5l-3 7h6zM20 5l-3 7h6z"/><path d="M1 12a3 2 0 0 0 6 0M17 12a3 2 0 0 0 6 0" stroke="var(--blue-deep)"/></svg>Insurance<br>&amp; Legal</div>
  <div class="sep" style="left:362px;top:174px"></div>
  <div class="industry" style="left:361px;top:168px"><svg viewBox="0 0 24 24" fill="none" stroke="var(--navy)" stroke-width="1.2"><path d="M1 22V12h5v-3h4v13M10 22V15l5-3v10M15 22v-6h7v6zM1 22h22"/><rect x="7" y="1" width="12" height="5" rx="2.5" stroke="var(--blue-deep)"/></svg>Pulp &amp; Paper</div>

  <p class="abs callout">No matter the industry, we help clients<br>minimize risk and maximize performance.</p>
  <div class="dots" style="left:416px;top:258px"><i></i><i></i><i></i><i></i><i></i><i></i><i></i></div>
  <div class="dots" style="left:416px;top:263px"><i></i><i></i><i></i><i></i><i></i><i></i><i></i></div>
</section>

<!-- Why choose us -->
<section class="slide slide--why">
  <svg class="art" viewBox="0 0 516 290">
    <defs>
      <radialGradient id="globeGrad" cx=".62" cy=".5" r=".6">
        <stop offset="0" stop-color="#5a6fc4"/><stop offset=".55" stop-color="#1c2f74"/><stop offset="1" stop-color="#070f2e"/>
      </radialGradient>
    </defs>
    <polygon points="404,0 413,0 330,123 424,290 415,290 322,123" fill="#d9dde2"/>
    <polygon points="413,0 516,0 516,290 424,290 330,123" fill="url(#globeGrad)" role="img" aria-label="Illustration: Earth from space wrapped in a glowing network of connections"/>
    <polygon points="323,290 383,230 417,290" fill="var(--blue-deep)"/>
  </svg>
  <h2 class="abs title" style="left:31px;top:30px">WHY CLIENTS CHOOSE US</h2>
  <p class="abs subtitle" style="left:31px;top:53px">Confidence Through Partnership</p>

  <div class="reason" style="top:86px"><div class="reason__icon"><svg width="11" height="11" viewBox="0 0 12 12" fill="none" stroke="#fff" stroke-width="1"><path d="M6 9.5S2 7 2 4.5A2 2 0 0 1 6 3.5a2 2 0 0 1 4 1C10 7 6 9.5 6 9.5z"/></svg></div><div><h3>Trust &amp; Independence</h3><p>Objective testing and transparent<br>reporting you can rely on.</p></div></div>
  <div class="reason" style="top:124px"><div class="reason__icon"><svg width="11" height="11" viewBox="0 0 12 12" fill="none" stroke="#fff" stroke-width="1"><circle cx="6" cy="6" r="4"/><circle cx="6" cy="6" r="1.5"/><path d="M6 0v3M6 9v3M0 6h3M9 6h3"/></svg></div><div><h3>Technical Accuracy</h3><p>Highly skilled specialists using advanced<br>methodologies and equipment.</p></div></div>
  <div class="reason" style="top:164px"><div class="reason__icon"><svg width="11" height="11" viewBox="0 0 12 12" fill="none" stroke="#fff" stroke-width="1"><circle cx="6" cy="6" r="4.5"/><path d="M6 3v3l2 1.5"/></svg></div><div><h3>Fast Turnaround</h3><p>Efficient processes that keep projects<br>moving and reduce downtime.</p></div></div>
  <div class="reason" style="top:202px"><div class="reason__icon"><svg width="11" height="11" viewBox="0 0 12 12" fill="none" stroke="#fff" stroke-width="1"><path d="M2 10V7M4.5 10V5.5M7 10V4M9.5 10V2.5M1 10.5h10"/></svg></div><div><h3>Value Beyond Compliance</h3><p>Actionable insights that improve quality,<br>performance, and long-term reliability.</p></div></div>
  <div class="reason" style="top:240px"><div class="reason__icon"><svg width="11" height="11" viewBox="0 0 12 12" fill="none" stroke="#fff" stroke-width="1"><circle cx="6" cy="6" r="4.5"/><ellipse cx="6" cy="6" rx="2" ry="4.5"/><path d="M1.5 6h9"/></svg></div><div><h3>Global Reach</h3><p>Serving organizations across the United States and<br>international markets with consistent, dependable expertise.</p></div></div>
</section>

<!-- Contact -->
<section class="slide slide--contact">
  <svg class="art" viewBox="0 0 516 290">
    <defs>
      <linearGradient id="dealGrad" x1="0" y1="0" x2="1" y2="1">
        <stop offset="0" stop-color="#2c4f86"/><stop offset=".5" stop-color="#b79a86"/><stop offset="1" stop-color="#1b3561"/>
      </linearGradient>
    </defs>
    <polygon points="315,0 516,0 516,290 356,290 420,232" fill="url(#dealGrad)" role="img" aria-label="Photograph: two business partners shaking hands"/>
    <polygon points="356,290 516,132 516,290" fill="var(--blue-deep)"/>
    <polygon points="376,290 516,150 516,160 386,290" fill="var(--blue)"/>
  </svg>
  <h2 class="abs contact__title">LET'S BUILD<br>CONFIDENCE<br><span>TOGETHER</span></h2>
  <div class="rule" style="left:29px;top:117px"></div>
  <p class="abs body-copy" style="left:29px;top:131px;width:172px">Whether validating products, ensuring regulatory compliance, investigating failures, or improving operational reliability, we provide the expertise and responsiveness needed to help you succeed.</p>

  <div class="benefit" style="left:16px;top:185px"><svg viewBox="0 0 20 20" fill="none" stroke="var(--navy)" stroke-width="1.2"><rect x="3" y="4" width="14" height="14" rx="2"/><path d="M7 2v4M13 2v4M7 11l2 2 4-4" stroke="var(--blue-deep)"/></svg>Reliable Results</div>
  <div class="benefit" style="left:105px;top:185px"><svg viewBox="0 0 20 20" fill="none" stroke="var(--navy)" stroke-width="1.2"><circle cx="9" cy="9" r="7.5"/><path d="M9 4v5l3 2"/><circle cx="15" cy="15" r="3" fill="#fff"/><path d="M15 13.5v2M15 16.5v.5"/></svg>Faster Decisions</div>
  <div class="benefit" style="left:192px;top:185px"><svg viewBox="0 0 20 20" fill="none" stroke="var(--navy)" stroke-width="1.2"><path d="M10 3L2 17h16z"/><path d="M10 8v4M10 14v1" stroke="var(--blue-deep)"/><path d="M3 5l2 1M17 5l-2 1M10 0v1.5"/></svg>Reduced Risk</div>
  <div class="benefit" style="left:282px;top:185px"><svg viewBox="0 0 20 20" fill="none" stroke="var(--navy)" stroke-width="1.2"><path d="M3 11V9a7 7 0 0 1 14 0v2"/><rect x="2" y="10" width="3" height="5" rx="1"/><rect x="15" y="10" width="3" height="5" rx="1"/><path d="M16.5 15c0 2-2 3-5 3"/></svg>Long-Term<br>Technical Support</div>

  <div class="abs cta">CONTACT US</div>
  <svg class="abs cta-arrow" width="10" height="30" viewBox="0 0 10 30"><path d="M0 0h3l7 15-7 15H0l7-15z" fill="var(--blue-deep)"/></svg>
  <div class="reach" style="left:143px"><svg width="15" height="15" viewBox="0 0 16 16" fill="none" stroke="var(--navy)" stroke-width="1"><circle cx="8" cy="8" r="7"/><ellipse cx="8" cy="8" rx="3" ry="7"/><path d="M1 8h14"/></svg><div><small>Website:</small><b>qorvenlab.com</b></div></div>
  <div class="reach" style="left:233px"><svg width="13" height="14" viewBox="0 0 14 15" fill="none" stroke="var(--navy)" stroke-width="1"><rect x="1" y="1" width="12" height="13" rx="1"/><path d="M4 4c0 4 3 7 6 7l1-2-2-1-1 1c-1-.5-2-1.5-2.5-2.5l1-1-1-2z"/></svg><div><small>Phone</small><b>+1 (555) 014-2290</b></div></div>
</section>

</body>
</html>
```